Corvane Lift Inc Website Deisgn

We are a new small elevator contracting company.
We would like a full website designed similar to
http://pellusk-lifts.example or https://www.marbolt-hoistworks.example/
In addition to contents found on the above webpages.. we would like a section for project gallery etc.... have fun with it ... make it professional

Target Market(s)

Elevator Consultants - Property managers - Condo Boards - Commercial office buildings

Coding

Coded - Design and coding required

Number of Pages Required

5+ page

Requirements
Must have
• Navigation Bar.. Be view able via mobile ..Should be pictures of Tall Office buildings in background.. Toronto city skyline etc....

Have Fun!

```html
<!DOCTYPE html>
<html lang="en">
<head>
<meta charset="utf-8">
<title>Corvane Lift Inc</title>
<link href="https://fonts.googleapis.com/css2?family=Bebas+Neue&family=Lato:wght@400;700&family=Ubuntu:wght@400;500&display=swap" rel="stylesheet">
<style>
:root{
  --blue:#4a7db8;
  --page:#f1f1f1;
  --ink:#2b2b2b;
  --muted:#3c3c3c;
  --dark:#2f2f2f;
  --white:#ffffff;
}
*{margin:0;padding:0;box-sizing:border-box}
html,body{width:1200px;height:3523px;overflow:hidden}
body{background:var(--page);font-family:'Lato',sans-serif;color:var(--muted);position:relative}
.abs{position:absolute}
.btn{position:absolute;display:flex;align-items:center;justify-content:center;background:var(--blue);color:var(--white);border-radius:20px;font-size:13px;font-family:'Lato',sans-serif}
.heading{position:absolute;left:0;width:1200px;text-align:center;font-family:'Bebas Neue',sans-serif;font-size:38px;letter-spacing:1px;color:var(--ink)}
.subheading{position:absolute;left:0;width:1200px;text-align:center;font-size:13px}
.copy{font-size:12.5px;line-height:15px}
.copy p{margin-bottom:15px}

/* header */
.site-header{position:absolute;top:0;left:0;width:1200px;height:117px;background:var(--page)}
.brand{position:absolute;left:75px;top:26px;display:flex;align-items:center;gap:8px}
.brand-mark{width:44px;height:44px;border:4px solid var(--ink);border-radius:50%}
.brand-name{font-family:'Lato',sans-serif;font-weight:700;font-size:27px;color:var(--ink);letter-spacing:1px}
.nav{position:absolute;top:52px;left:534px;display:flex;gap:0;font-size:13px;color:var(--muted)}
.nav a{position:absolute;white-space:nowrap;color:inherit;text-decoration:none}
.nav .active{color:var(--blue);border-bottom:2px solid var(--blue);padding-bottom:3px}

/* hero */
.hero{position:absolute;top:117px;left:0;width:1200px;height:613px;overflow:hidden}
.hero-photo{position:absolute;inset:0;background:linear-gradient(120deg,#6e6660 0%,#3d4550 35%,#55606c 60%,#8d8c88 100%)}
.hero-title{position:absolute;top:240px;left:0;width:1245px;text-align:center;font-family:'Ubuntu',sans-serif;font-size:35px;color:var(--white)}
.hero-sub{position:absolute;top:285px;left:0;width:1200px;text-align:center;font-size:12px;line-height:15px;color:var(--white)}
.hero-dots{position:absolute;right:23px;top:216px;display:flex;flex-direction:column;gap:8px}
.hero-dots span{width:8px;height:8px;border:1px solid var(--white);border-radius:50%}
.hero-dots span.on{background:var(--white)}

/* about */
.about-kicker{position:absolute;left:75px;top:850px;display:flex;align-items:center;gap:20px;font-family:'Bebas Neue',sans-serif;font-size:21px;color:var(--ink)}
.about-kicker i{display:block;width:47px;height:3px;background:var(--blue)}
.about-copy{position:absolute;left:113px;top:900px;width:445px}
.about-photo{position:absolute;left:637px;top:851px;width:452px;height:300px;background:linear-gradient(180deg,#8ea1b4 0%,#b8a9b4 45%,#3f5866 75%,#263840 100%)}

/* services */
.slider-arrows{position:absolute;left:1044px;top:1236px;display:flex;gap:14px}
.card{position:absolute;top:1294px;width:313px;height:378px;background:var(--white);text-align:center}
.card.featured{background:var(--blue);color:var(--white)}
.card-photo{position:absolute;left:12px;top:11px;width:289px;height:207px}
.card-title{position:absolute;top:236px;left:0;width:100%;font-family:'Ubuntu',sans-serif;font-size:19px;color:var(--ink)}
.card.featured .card-title{color:var(--white)}
.card-rule{position:absolute;top:264px;left:132px;width:50px;height:2px;background:var(--ink)}
.card.featured .card-rule{background:var(--white)}
.card-text{position:absolute;top:280px;left:30px;width:253px;font-size:12.5px;line-height:18px}
.card-arrow{position:absolute;top:348px;left:148px}

/* choose */
.choose{position:absolute;top:1755px;left:0;width:1200px;height:500px;background:linear-gradient(90deg,#c9c9c9 0%,#dcdcdc 45%,#cfcfcf 100%)}
.choose-photo{position:absolute;left:505px;top:0;width:695px;height:500px;background:linear-gradient(90deg,#bdbdbd,#e6e6e6 30%,#a9a9a9 55%,#e0e0e0 80%,#b5b5b5)}
.choose-title{position:absolute;left:100px;top:110px;font-family:'Bebas Neue',sans-serif;font-size:36px;letter-spacing:1px;color:var(--ink)}
.choose-rule{position:absolute;left:100px;top:155px;width:45px;height:3px;background:var(--blue)}
.choose-copy{position:absolute;left:100px;top:181px;width:395px}

/* gallery */
.tile{position:absolute;top:2373px;width:229px;height:319px}
.tile-overlay{position:absolute;left:12px;bottom:20px;color:var(--white)}
.tile-overlay h4{font-family:'Bebas Neue',sans-serif;font-size:15px;font-weight:400;letter-spacing:.5px}
.tile-overlay i{display:block;width:38px;height:2px;background:var(--white);margin:4px 0 10px}
.tile-overlay p{font-size:11px;line-height:14px;width:190px}

/* contact */
.field{position:absolute;width:316px;height:44px;border-bottom:1px solid #e6e6e6;font-size:12px;padding:14px 0 0 14px;color:var(--muted)}
.field.message{width:313px;height:145px}

/* footer */
.footer-curve{position:absolute;top:3120px;left:0}
.footer{position:absolute;top:3240px;left:0;width:1200px;height:212px;background:var(--dark);color:var(--white)}
.footer-brand{position:absolute;left:113px;top:5px;display:flex;align-items:center;gap:6px}
.footer-brand .brand-mark{border-color:var(--white);width:42px;height:42px}
.footer-brand .brand-name{color:var(--white);font-size:25px}
.footer h5{position:absolute;font-family:'Bebas Neue',sans-serif;font-size:16px;font-weight:400;letter-spacing:.5px}
.footer h5::after{content:"";display:block;width:34px;height:2px;background:var(--white);margin-top:5px}
.footer .copy{font-size:12px;line-height:15px}
.quick-links{position:absolute;left:432px;top:53px;list-style:none;font-size:12.5px;line-height:22.5px}
.quick-links li::before{content:"•";margin-right:8px}
.contact-list{position:absolute;left:602px;top:53px;list-style:none;font-size:12px;line-height:24px}
.contact-list li{display:flex;align-items:center;gap:10px}
.contact-list svg{flex:none}
.sub-input{position:absolute;left:857px;top:83px;width:231px;height:31px;border-radius:16px;background:var(--white);color:var(--muted);font-size:12px;padding:8px 14px}
.sub-btn{position:absolute;left:857px;top:125px;width:231px;height:31px;border-radius:16px;background:var(--blue);display:flex;align-items:center;justify-content:center;font-size:13px;letter-spacing:1px}
.bottom-bar{position:absolute;top:3452px;left:0;width:1200px;height:71px;background:var(--page)}
.bottom-bar .legal{position:absolute;left:110px;top:24px;font-size:12px;color:var(--ink)}
.socials{position:absolute;left:873px;top:16px;display:flex;gap:14px}
.socials span{width:31px;height:31px;border-radius:50%;background:var(--dark)}
.socials span.alt{background:var(--blue)}
</style>
</head>
<body>

<header class="site-header">
  <div class="brand"><span class="brand-mark"></span><span class="brand-name">CORVANE LIFT INC</span></div>
  <nav class="nav">
    <a class="active" style="left:0">Home</a>
    <a style="left:77px">About us</a>
    <a style="left:170px">Services</a>
    <a style="left:261px">News</a>
    <a style="left:334px">Contact us</a>
  </nav>
  <div class="btn" style="left:978px;top:40px;width:147px;height:38px;font-size:14px">Get a Quote</div>
</header>

<section class="hero">
  <div class="hero-photo" role="img" aria-label="Glass panoramic elevator inside a modern steel and glass office atrium"></div>
  <svg class="abs" style="left:0;top:0" width="1200" height="613" viewBox="0 0 1200 613">
    <path d="M0,395 C250,520 650,600 1200,470 L1200,613 L0,613 Z" fill="#050505"/>
    <path d="M0,458 C250,545 520,592 900,598 L900,613 L0,613 Z" fill="#4a7db8"/>
    <path d="M0,567 C300,612 650,622 1200,600 L1200,613 L0,613 Z" fill="#f1f1f1"/>
  </svg>
  <h1 class="hero-title" style="font-weight:500">Be safe with us</h1>
  <p class="hero-sub">Lorem Ipsum is simply dummy text of the printing<br>in thenext typesetting industry.</p>
  <div class="btn" style="left:518px;top:331px;width:165px;height:35px">Read More</div>
  <div class="hero-dots"><span class="on"></span><span></span><span></span><span></span></div>
</section>

<section class="about">
  <h2 class="heading" style="top:780px">About Us</h2>
  <div class="about-kicker"><i></i>What is Lorem Ipsum?</div>
  <div class="about-copy copy">
    <p>Lorem Ipsum is simply dummy text of the printing and typesetting industry has been the industry's standard dummy text ever since the 1500s,</p>
    <p>when an unknown printer took a galley of type and scrambled it to make a type specimen book. It has survived not only five centuries, but also the leap into electronic typesetting, remaining essentially unchanged. It popularised in the 1960s</p>
    <p>with the release of Letraset sheets containing Lorem Ipsum passages, and more recently with desktop publishing software Aldus PageMaker including versions of Lorem Ipsum.</p>
  </div>
  <div class="btn" style="left:112px;top:1096px;width:163px;height:37px">Read More</div>
  <div class="about-photo" role="img" aria-label="City skyline with a tall communications tower at dusk"></div>
</section>

<section class="services">
  <h2 class="heading" style="top:1218px">Services</h2>
  <p class="subheading" style="top:1264px">Lorem Ipsum is simply dummy text of the printing</p>
  <div class="slider-arrows">
    <svg width="18" height="12" viewBox="0 0 18 12"><path d="M17,6 H2 M6,1 L1,6 L6,11" fill="none" stroke="#1a1a1a" stroke-width="1.8"/></svg>
    <svg width="18" height="12" viewBox="0 0 18 12"><path d="M1,6 H16 M12,1 L17,6 L12,11" fill="none" stroke="#4a7db8" stroke-width="1.8"/></svg>
  </div>

  <article class="card" style="left:102px">
    <div class="card-photo" role="img" aria-label="Businessman pressing a button inside a glass elevator" style="background:linear-gradient(135deg,#d8c7a8,#2e3f58 55%,#9fb0c2)"></div>
    <h3 class="card-title" style="font-weight:400">Modernization</h3><i class="card-rule"></i>
    <p class="card-text">Lorem Ipsum is simply dummy text of the printing and typesetting industry. Lorem Ipsum has been the industry's.</p>
    <svg class="card-arrow" width="17" height="10" viewBox="0 0 17 10"><path d="M1,5 H15 M11,1 L15,5 L11,9" fill="none" stroke="#4a7db8" stroke-width="1.6"/></svg>
  </article>

  <article class="card featured" style="left:444px">
    <div class="card-photo" role="img" aria-label="Elevator traction machine in a machine room" style="background:linear-gradient(135deg,#e5d6b0,#3a4a44 45%,#2f8a5c 60%,#b9b9b9)"></div>
    <h3 class="card-title" style="font-weight:400">Maintenance</h3><i class="card-rule"></i>
    <p class="card-text">Lorem Ipsum is simply dummy text of the printing and typesetting industry. Lorem Ipsum has been the industry's.</p>
    <svg class="card-arrow" width="17" height="10" viewBox="0 0 17 10"><path d="M1,5 H15 M11,1 L15,5 L11,9" fill="none" stroke="#fff" stroke-width="1.6"/></svg>
  </article>

  <article class="card" style="left:787px">
    <div class="card-photo" role="img" aria-label="Technician in a hard hat servicing elevator equipment" style="background:linear-gradient(135deg,#d98a3a,#3b4658 40%,#5b6b84 70%,#c9ccd2)"></div>
    <h3 class="card-title" style="font-weight:400">Service &amp; Repair</h3><i class="card-rule"></i>
    <p class="card-text">Lorem Ipsum is simply dummy text of the printing and typesetting industry. Lorem Ipsum has been the industry's.</p>
    <svg class="card-arrow" width="17" height="10" viewBox="0 0 17 10"><path d="M1,5 H15 M11,1 L15,5 L11,9" fill="none" stroke="#4a7db8" stroke-width="1.6"/></svg>
  </article>
</section>

<section class="choose">
  <div class="choose-photo" role="img" aria-label="Two open stainless steel elevator cars in a bright grey lobby"></div>
  <h2 class="choose-title">Choose from the best</h2>
  <i class="choose-rule"></i>
  <div class="choose-copy copy">
    <p>Lorem Ipsum is simply dummy text of the printing and typesetting industry has been the industry's standard dummy text ever since the 1500s,</p>
    <p>when an unknown printer took a galley of type and scrambled it make a type specimen book. It has survived not only five centuries, but also the leap into electronic typesetting, remaining essentially unchanged. It popularised in the 1960s</p>
  </div>
  <div class="btn" style="left:96px;top:331px;width:163px;height:37px">Read More</div>
</section>

<section class="gallery">
  <h2 class="heading" style="top:2290px">Gallery</h2>
  <p class="subheading" style="top:2334px">Lorem Ipsum is simply dummy of the printing</p>
  <div class="tile" style="left:112px;background:linear-gradient(90deg,#8a7a62,#e8e6df 45%,#c9c2b2 80%,#ede9e0)" role="img" aria-label="Brushed metal elevator doors beside a potted plant"></div>
  <div class="tile" style="left:361px;background:linear-gradient(90deg,#3a3a3a,#1f1f1f 55%,#2a2a2a)" role="img" aria-label="Dark elevator entrance in a black tiled wall">
    <div class="tile-overlay"><h4>Project Name</h4><i></i><p>Lorem Ipsum is simply dummy text typessetting industry.</p>
      <svg width="14" height="14" viewBox="0 0 14 14" style="margin-top:10px"><circle cx="7" cy="7" r="6" fill="none" stroke="#fff"/><path d="M6,4.5 L8.5,7 L6,9.5" fill="none" stroke="#fff"/></svg></div>
  </div>
  <div class="tile" style="left:610px;background:linear-gradient(120deg,#1f2d44,#9fb8cf 45%,#e0e8ef 70%,#d89040)" role="img" aria-label="Hand pressing a floor button on a glass elevator panel"></div>
  <div class="tile" style="left:859px;background:linear-gradient(90deg,#d7d9de,#4a4c58 35%,#c9cbd2 55%,#3e4050 75%,#d9dae0)" role="img" aria-label="Pair of dark elevator doors in a pale corridor"></div>
  <div class="btn" style="left:528px;top:2723px;width:147px;height:37px">View More</div>
</section>

<section class="contact">
  <h2 class="heading" style="top:2802px;font-size:34px">Get in Touch</h2>
  <div class="field" style="left:272px;top:2879px">Name*</div>
  <div class="field" style="left:272px;top:2935px">Phone*</div>
  <div class="field" style="left:272px;top:2992px">Email*</div>
  <div class="field message" style="left:612px;top:2879px">Message</div>
  <div class="btn" style="left:532px;top:3046px;width:148px;height:38px;font-weight:700">Send</div>
</section>

<svg class="footer-curve" width="1200" height="125" viewBox="0 0 1200 125">
  <path d="M330,40 C650,-5 1000,10 1200,55 L1200,125 L330,125 Z" fill="#4a7db8"/>
  <path d="M0,122 C250,45 650,30 1060,55 C1120,80 1170,105 1200,125 L0,125 Z" fill="#050505"/>
  <path d="M0,125 L0,110 C300,75 700,70 1200,118 L1200,125 Z" fill="#2f2f2f"/>
</svg>

<footer class="footer">
  <div class="footer-brand"><span class="brand-mark"></span><span class="brand-name">CORVANE LIFT INC</span></div>
  <p class="copy abs" style="left:113px;top:78px;width:235px">Lorem Ipsum is simply dummy text next of the printing and typesetting industry has been the industry's</p>
  <svg class="abs" style="left:113px;top:128px" width="17" height="10" viewBox="0 0 17 10"><path d="M1,5 H15 M11,1 L15,5 L11,9" fill="none" stroke="#fff" stroke-width="1.6"/></svg>

  <h5 style="left:432px;top:5px">Quick Link</h5>
  <ul class="quick-links"><li>Home</li><li>About us</li><li>Services</li><li>News</li><li>Contact us</li></ul>

  <h5 style="left:602px;top:5px">Quick Contact</h5>
  <ul class="contact-list">
    <li><svg width="12" height="14" viewBox="0 0 12 14"><path d="M6,13 C2,8 1.5,6.5 1.5,5 A4.5,4.5 0 0 1 10.5,5 C10.5,6.5 10,8 6,13 Z" fill="none" stroke="#fff"/><circle cx="6" cy="5" r="1.6" fill="none" stroke="#fff"/></svg>88 Harlow Quay Street</li>
    <li style="padding-left:22px">Brennick, Alberta</li>
    <li><svg width="13" height="10" viewBox="0 0 13 10"><rect x="1" y="3" width="11" height="6" rx="1" fill="none" stroke="#fff"/><path d="M1,3 C3,0 10,0 12,3" fill="none" stroke="#fff"/></svg>555 014 2280</li>
    <li><svg width="13" height="10" viewBox="0 0 13 10"><rect x="1" y="3" width="11" height="6" rx="1" fill="none" stroke="#fff"/><path d="M1,3 C3,0 10,0 12,3" fill="none" stroke="#fff"/></svg>555 017 6642</li>
    <li><svg width="13" height="10" viewBox="0 0 13 10"><rect x="0.5" y="0.5" width="12" height="9" fill="none" stroke="#fff"/><path d="M0.5,0.5 L6.5,5.5 L12.5,0.5" fill="none" stroke="#fff"/></svg>hello@corvanelift.example</li>
  </ul>

  <h5 style="left:857px;top:5px">Subscribe</h5>
  <p class="copy abs" style="left:858px;top:45px;width:235px">Lorem Ipsum is simply dummy text next of the printing and typesetting.</p>
  <div class="sub-input">Email Here</div>
  <div class="sub-btn">Send Now</div>
</footer>

<div class="bottom-bar">
  <p class="legal">Copyright © 2020 Corvane Lift Inc. All Right Reserved</p>
  <div class="socials" aria-label="Social links"><span class="alt"></span><span></span><span></span><span></span><span></span></div>
</div>

</body>
</html>
```